We go to sell aluminum with a lot of effects, cement, marble, water, sand ... we need an image for a sample book and its name will be VORENTA MIRAGE.
The archive we upload is the image of our sample book of aluminum with wood effect.

```html
<!DOCTYPE html>
<html lang="en">
<head>
<meta charset="UTF-8">
<title>Vorenta Mirage – Sample Book Cover</title>
<link rel="stylesheet" href="https://fonts.googleapis.com/css2?family=Libre+Baskerville:wght@400;700&display=swap">
<style>
  :root {
    --page-bg: #e9ecf1;
    --cover-dark: #2b2c2e;
    --cover-mid: #4a4b4d;
    --glitter-light: #d9d9da;
    --glitter-mid: #8f9092;
    --spine: #1d1e20;
    --title-white: #f6f6f4;
    --subtitle-grey: #c9cacc;
  }
  * { margin: 0; padding: 0; box-sizing: border-box; }
  html, body {
    width: 1200px;
    height: 840px;
    overflow: hidden;
    background: var(--page-bg);
  }
  .stage {
    position: relative;
    width: 1200px;
    height: 840px;
  }
  .book-cover {
    position: absolute;
    left: 250px;
    top: 50px;
    width: 740px;
    height: 740px;
    background: var(--cover-dark);
    overflow: hidden;
    box-shadow: 0 18px 40px rgba(30, 35, 45, 0.25);
  }
  .cover-photo {
    position: absolute;
    inset: 0;
    background:
      radial-gradient(ellipse 70% 30% at 78% 62%, rgba(235,235,236,0.55), rgba(235,235,236,0) 70%),
      radial-gradient(ellipse 90% 35% at 70% 88%, var(--glitter-light), rgba(200,200,202,0) 75%),
      linear-gradient(180deg, var(--cover-dark) 0%, var(--cover-dark) 42%, var(--cover-mid) 58%, var(--glitter-mid) 78%, #6d6e70 100%);
  }
  .cover-spine {
    position: absolute;
    left: 0;
    top: 0;
    width: 22px;
    height: 100%;
    background: linear-gradient(90deg, var(--spine), #3a3b3d 70%, #262729);
  }
  .brand-mark {
    position: absolute;
    top: 130px;
    left: 0;
    right: 0;
    display: flex;
    align-items: center;
    justify-content: center;
    gap: 14px;
  }
  .brand-mark-dot {
    width: 18px;
    height: 18px;
    border-radius: 50%;
    background: var(--title-white);
  }
  .brand-mark-name {
    font-family: "Libre Baskerville", serif;
    font-weight: 700;
    font-size: 34px;
    letter-spacing: 6px;
    color: var(--title-white);
  }
  .cover-titles {
    position: absolute;
    top: 282px;
    left: 0;
    right: 0;
    text-align: center;
  }
  .company-line {
    font-family: "Libre Baskerville", serif;
    font-weight: 400;
    font-size: 26px;
    letter-spacing: 8px;
    color: var(--subtitle-grey);
    line-height: 1.2;
  }
  .collection-title {
    margin-top: 10px;
    font-family: "Libre Baskerville", serif;
    font-weight: 400;
    font-size: 64px;
    letter-spacing: 6px;
    color: var(--title-white);
    line-height: 1.1;
  }
</style>
</head>
<body>
  <main class="stage">
    <section class="book-cover">
      <div class="cover-photo" role="img" aria-label="Close-up photograph of silver glitter sand on a dark surface with soft bokeh highlights"></div>
      <div class="cover-spine"></div>
      <div class="brand-mark">
        <span class="brand-mark-dot"></span>
        <span class="brand-mark-name">VORENTA</span>
      </div>
      <div class="cover-titles">
        <h1 class="company-line">ALUMINIOS VORENTA</h1>
        <h2 class="collection-title">MIRAGE</h2>
      </div>
    </section>
  </main>
</body>
</html>
```